Label design for our new range of organic honey.

We need a design for honey jars and tubs. The label needs to indicate we are located in the Western Australia. The design needs to be elegant, modern and attracting high end customers that focus on quality.

Need extra days to review

```html
<!DOCTYPE html>
<html lang="en">
<head>
<meta charset="utf-8">
<title>Coastal Amber Honey – Jar Label</title>
<link rel="stylesheet" href="https://fonts.googleapis.com/css2?family=Cinzel:wght@400&family=Oswald:wght@300&display=swap">
<style>
  :root {
    --backdrop: #2b2b2b;
    --label-black: #120e0e;
    --gold: #e9a51a;
    --gold-soft: #c98a12;
    --bee-amber: #b07a1c;
  }
  html, body {
    margin: 0;
    padding: 0;
    width: 1200px;
    height: 1200px;
    overflow: hidden;
    background: var(--backdrop);
  }
  .label-canvas {
    display: block;
    width: 1200px;
    height: 1200px;
  }
  .label-body { fill: var(--label-black); }
  .frame-line {
    fill: none;
    stroke: var(--gold);
    stroke-width: 2;
  }
  .rule {
    stroke: var(--gold);
    stroke-width: 1.5;
  }
  .brand-mark {
    font-family: 'Cinzel', serif;
    font-size: 26px;
    fill: var(--gold);
    letter-spacing: 2px;
  }
  .tagline {
    font-family: 'Oswald', sans-serif;
    font-weight: 300;
    font-size: 27px;
    fill: var(--gold);
    letter-spacing: 0.5px;
  }
  .product-title {
    font-family: 'Cinzel', serif;
    font-size: 74px;
    fill: var(--gold);
    letter-spacing: 1px;
  }
  .est-year {
    font-family: 'Oswald', sans-serif;
    font-weight: 300;
    font-size: 24px;
    fill: var(--gold);
  }
  .bee-emblem { fill: var(--label-black); stroke: var(--gold); stroke-width: 2; }
  .bee-art { fill: var(--bee-amber); opacity: 0.55; }
</style>
</head>
<body>
<svg class="label-canvas" viewBox="0 0 1200 1200" xmlns="http://www.w3.org/2000/svg">
  <!-- hexagonal label -->
  <polygon class="label-body" points="600,90 1000,320 1000,880 600,1110 200,880 200,320"/>
  <polygon class="frame-line" points="600,142 955,346 955,854 600,1058 245,854 245,346"/>
  <polygon class="frame-line" points="600,160 940,355 940,845 600,1040 260,845 260,355"/>

  <!-- brand mark -->
  <text class="brand-mark" x="600" y="262" text-anchor="middle">CA HONEY</text>

  <!-- tagline -->
  <text class="tagline" x="600" y="372" text-anchor="middle">LOCALLY SOURCED IN WESTERN AUSTRALIA</text>
  <line class="rule" x1="482" y1="432" x2="718" y2="432"/>

  <!-- product name -->
  <text class="product-title" x="600" y="548" text-anchor="middle">COASTAL</text>
  <text class="product-title" x="600" y="630" text-anchor="middle">AMBER HONEY</text>

  <!-- established line with bee emblem -->
  <line class="rule" x1="395" y1="822" x2="500" y2="822"/>
  <line class="rule" x1="700" y1="822" x2="805" y2="822"/>
  <text class="est-year" x="448" y="808" text-anchor="middle">EST.</text>
  <text class="est-year" x="752" y="808" text-anchor="middle">2023</text>

  <polygon class="bee-emblem" points="600,708 700,766 700,882 600,940 500,882 500,766"/>
  <polygon class="bee-art" role="img" aria-label="Illustration of a golden honey bee with sprigs of native flowers" points="600,740 672,782 672,866 600,908 528,866 528,782"/>
</svg>
</body>
</html>
```